Real Estate "For Sale" Sign for construction company

We need a sign that we can use to hang on a post and place on the road when we sell a property. The sign will be simple and will need to mainly feature our logo (files attached), as well as the words "For Sale", and then our phone number "(555) 617 3489". The sign will hang on a post that'll look something like the attached picture.

Target Market(s)

Home buyers

Industry/Entity Type

Real Estate

Font styles to use
Serif
Sans Serif

Colors
0054AA
0677BA
7BADD7
CADEEF
E8F1F8
0094D4
00A9DD
6FCCEA
C7EBF8
E9F6FB

Requirements
Must have
• For Sale & our phone number

```html
<!DOCTYPE html>
<html lang="en">
<head>
<meta charset="utf-8">
<title>Ridgeline Summit Properties – For Sale Signs</title>
<link rel="stylesheet" href="https://fonts.googleapis.com/css2?family=Montserrat:wght@400;500;800&display=swap">
<style>
  :root {
    --navy: #14204a;
    --brand-blue: #1a80c4;
    --phone-blue: #0054aa;
    --sky-light: #e9f6fb;
    --sky-mid: #c7ebf8;
    --sky-deep: #92d5f5;
    --sky-flat: #cdedfb;
    --ridge-light: #8fd7f6;
    --ridge-mid: #16a4dc;
    --ridge-dark: #0054aa;
  }
  * { margin: 0; padding: 0; box-sizing: border-box; }
  html, body {
    width: 1200px;
    height: 721px;
    overflow: hidden;
    background: var(--navy);
    font-family: "Montserrat", Arial, sans-serif;
  }
  .sign {
    position: absolute;
    top: 91px;
    width: 512px;
    height: 539px;
    overflow: hidden;
    text-align: center;
  }
  .sign--gradient {
    left: 74px;
    background: linear-gradient(135deg, var(--sky-light) 0%, var(--sky-mid) 40%, var(--sky-deep) 100%);
  }
  .sign--flat {
    left: 613px;
    background: var(--sky-flat);
  }
  .brand {
    position: absolute;
    top: 68px;
    left: 0;
    right: 0;
    color: var(--brand-blue);
    font-weight: 400;
  }
  .brand__dot {
    display: block;
    width: 56px;
    height: 56px;
    margin: 0 auto 10px;
    border-radius: 50%;
    background: var(--brand-blue);
  }
  .brand__name {
    display: block;
    font-size: 29px;
    line-height: 1;
    letter-spacing: 0.5px;
  }
  .brand__tagline {
    display: block;
    margin-top: 12px;
    font-size: 10px;
    letter-spacing: 11px;
    padding-left: 11px;
    line-height: 1;
  }
  .headline {
    position: absolute;
    top: 226px;
    left: 0;
    right: 0;
    font-size: 80px;
    font-weight: 800;
    line-height: 1;
    color: var(--navy);
    letter-spacing: 1px;
  }
  .phone {
    position: absolute;
    top: 311px;
    left: 0;
    right: 0;
    font-size: 58px;
    font-weight: 500;
    line-height: 1;
    color: var(--phone-blue);
  }
  .ridges {
    position: absolute;
    left: 18px;
    right: 16px;
    bottom: 0;
    height: 127px;
    border-radius: 120px 120px 0 0;
    background: linear-gradient(180deg, var(--ridge-light) 0%, var(--ridge-mid) 55%, var(--ridge-dark) 100%);
  }
</style>
</head>
<body>
  <section class="sign sign--gradient">
    <div class="brand">
      <span class="brand__dot"></span>
      <span class="brand__name">Ridgeline Summit</span>
      <span class="brand__tagline">PROPERTIES</span>
    </div>
    <h1 class="headline">FOR SALE</h1>
    <p class="phone">(555) 617 3489</p>
    <div class="ridges" role="img" aria-label="Layered blue mountain ridges with a snowy peak"></div>
  </section>

  <section class="sign sign--flat">
    <div class="brand">
      <span class="brand__dot"></span>
      <span class="brand__name">Ridgeline Summit</span>
      <span class="brand__tagline">PROPERTIES</span>
    </div>
    <h1 class="headline">FOR SALE</h1>
    <p class="phone">(555) 617 3489</p>
    <div class="ridges" role="img" aria-label="Layered blue mountain ridges with a snowy peak"></div>
  </section>
</body>
</html>
```